Tolliver Business Services Stationary
Letterhead, Business Card, Envelope
Tolliver Business Services Stationary -
Creative Brief
Simple
Dale Pruett
Bookkeeping and Tax Preparation
PO Box 4713 Seattle, WA 98109
dpruettpruett@tolliverllc.example
www.tolliverllc.example
The info for the business card is fake because this is not a private contest. I will provide the correct info when I finalize the contest. I need a standard sized business card, letterhead, and envelope. Finished artwork needs to be vector format. I have attached designs that I like and my company logo.
Maybe just the logo? reversed colors? I've attached samples and layouts the I like.

```html
<!DOCTYPE html>
<html lang="en">
<head>
<meta charset="utf-8">
<title>Tolliver Business Services Stationery</title>
<link href="https://fonts.googleapis.com/css2?family=Lato:wght@400;700&display=swap" rel="stylesheet">
<style>
  :root {
    --ink: #1f1f1f;
    --charcoal: #3a3a3a;
    --band: #454545;
    --mute: #6b6b6b;
    --paper: #ffffff;
    --ghost: #ececec;
    --rule: #bdbdbd;
    --page: #ffffff;
  }
  * { margin: 0; padding: 0; box-sizing: border-box; }
  html, body { width: 1200px; height: 901px; overflow: hidden; background: var(--page); }
  body { position: relative; font-family: "Lato", Arial, sans-serif; color: var(--ink); }

  .brand { display: flex; align-items: center; gap: 8px; }
  .brand-mark { width: 14px; height: 14px; background: var(--ink); }
  .brand-name { font-family: "Lato", Arial, sans-serif; font-weight: 700; color: var(--ink); letter-spacing: 1px; text-transform: uppercase; }

  /* Letterhead */
  .letterhead {
    position: absolute; left: 331px; top: 60px; width: 425px; height: 768px;
    background: var(--paper); box-shadow: 0 0 4px rgba(0,0,0,.35);
  }
  .letterhead .brand { position: absolute; left: 0; right: 0; top: 128px; justify-content: center; }
  .letterhead .brand-mark { width: 18px; height: 18px; }
  .letterhead .brand-name { font-size: 19px; }
  .letterhead-rule { position: absolute; left: 50px; right: 50px; top: 178px; border-top: 1px solid var(--rule); }
  .letter-subject { position: absolute; left: 0; right: 0; top: 212px; text-align: center; font-size: 12px; color: var(--charcoal); }
  .letter-body { position: absolute; left: 52px; width: 300px; top: 276px; font-size: 8px; line-height: 1.45; color: var(--charcoal); }
  .letter-body p { margin-bottom: 10px; }
  .signature { width: 70px; height: 30px; margin: 4px 0 2px; background: linear-gradient(90deg, #f2f2f2, #e6e6e6); }
  .letter-decor { position: absolute; left: 598px; }
  .letter-square { position: absolute; right: 50px; top: 590px; width: 96px; height: 96px; background: var(--charcoal); }
  .letter-address { position: absolute; left: 0; right: 0; bottom: 34px; text-align: center; font-size: 6px; color: var(--mute); }
  .letter-band {
    position: absolute; left: 0; right: 0; bottom: 0; height: 24px; background: var(--band);
    color: #e0e0e0; font-size: 6px; display: flex; justify-content: center; align-items: center; gap: 18px;
  }

  /* Envelope */
  .envelope {
    position: absolute; left: 787px; top: 180px; width: 185px; height: 564px;
    background: var(--paper); box-shadow: 0 0 4px rgba(0,0,0,.35); overflow: hidden;
  }
  .envelope-band { position: absolute; left: 0; top: 0; bottom: 0; width: 36px; background: var(--band); }
  .envelope .brand { position: absolute; left: 54px; top: 110px; }
  .envelope .brand-name { font-size: 13px; }
  .envelope-ghost { position: absolute; left: 80px; top: 250px; width: 150px; height: 150px; background: var(--ghost); transform: rotate(45deg); }
  .envelope-contact { position: absolute; left: 54px; top: 336px; font-size: 6px; line-height: 1.6; color: var(--charcoal); }
  .envelope-contact b { font-weight: 700; }
  .envelope-address { position: absolute; left: 54px; top: 420px; font-size: 6px; color: var(--mute); }

  /* Business card front */
  .card-front {
    position: absolute; left: 120px; top: 432px; width: 204px; height: 124px;
    background: var(--paper); box-shadow: 0 0 4px rgba(0,0,0,.35); overflow: hidden;
  }
  .card-front .brand { position: absolute; left: 14px; top: 16px; gap: 6px; }
  .card-front .brand-mark { width: 11px; height: 11px; }
  .card-front .brand-name { font-size: 11px; }
  .card-ghost { position: absolute; right: -20px; top: 40px; width: 90px; height: 90px; background: var(--ghost); transform: rotate(45deg); }
  .card-person { position: absolute; left: 14px; top: 44px; font-size: 6px; line-height: 1.5; color: var(--charcoal); }
  .card-name { font-size: 9px; font-weight: 700; color: var(--ink); }
  .card-title { margin-bottom: 4px; color: var(--mute); }
  .card-person b { font-weight: 700; }

  /* Business card back */
  .card-back {
    position: absolute; left: 98px; top: 590px; width: 204px; height: 124px;
    background: var(--charcoal); box-shadow: 0 2px 6px rgba(0,0,0,.4);
    transform: rotate(-17deg); transform-origin: left top; overflow: hidden;
  }
  .card-back .brand { position: absolute; left: 0; right: 0; top: 54px; justify-content: center; }
  .card-back .brand-mark { background: #fff; width: 12px; height: 12px; }
  .card-back .brand-name { color: #fff; font-size: 14px; }
</style>
</head>
<body>

<section class="card-front" aria-label="Business card front">
  <div class="card-ghost"></div>
  <div class="brand"><span class="brand-mark"></span><span class="brand-name">Tolliver</span></div>
  <div class="card-person">
    <div class="card-name">Dale Pruett</div>
    <div class="card-title">Owner</div>
    <div><b>Phone:</b> 206-555-0142</div>
    <div><b>Fax:</b> 206-555-0143</div>
    <div>PO Box 4713 Seattle,</div>
    <div>WA 98109</div>
    <div><b>Email:</b> dpruettpruett@tolliverllc.example</div>
    <div><b>Web:</b> www.tolliverllc.example</div>
  </div>
</section>

<section class="card-back" aria-label="Business card back">
  <div class="brand"><span class="brand-mark"></span><span class="brand-name">Tolliver</span></div>
</section>

<section class="letterhead" aria-label="Letterhead">
  <div class="brand"><span class="brand-mark"></span><span class="brand-name">Tolliver</span></div>
  <div class="letterhead-rule"></div>
  <h1 class="letter-subject">To whom it may concern</h1>
  <div class="letter-body">
    <p>To,<br>The Manager,</p>
    <p>This is to confirm that your quarterly books have been reconciled and your filing documents are now ready for signature at our office this week.</p>
    <p>Please review the enclosed summary and contact us with any questions before the deadline so we can finalize your return.</p>
    <p>We appreciate your continued trust in our bookkeeping and tax preparation services.</p>
    <p style="margin-bottom:0">Yours sincerely</p>
    <div class="signature" role="img" aria-label="Handwritten signature"></div>
    <div>Dale Pruett</div>
  </div>
  <div class="letter-square"></div>
  <div class="letter-address">PO Box 4713 Seattle, WA 98109</div>
  <div class="letter-band"><span>Phone 206-555-0142</span><span>Fax 206-555-0143</span></div>
</section>

<section class="envelope" aria-label="Envelope">
  <div class="envelope-band"></div>
  <div class="envelope-ghost"></div>
  <div class="brand"><span class="brand-mark"></span><span class="brand-name">Tolliver</span></div>
  <div class="envelope-contact">
    <div><b>Fax:</b> 206-555-0143</div>
    <div><b>Email:</b> dpruettpruett@tolliverllc.example</div>
    <div><b>Web:</b> www.tolliverllc.example</div>
    <div><b>Phone:</b> 206-555-0142</div>
  </div>
  <div class="envelope-address">PO Box 4713 Seattle, WA 98109</div>
</section>

</body>
</html>
```